VELVET ANVIL - BOOK COVER

I have written a book called VELVET ANVIL - HOW TO CLIMB PAST EVERY LIMIT AT FULL THROTTLE. I need a front cover design for the book. The book cover needs to be intriguing for someone to pick it up and read the first couple of pages. I want people to think about ACHIEVING SUCCESS when they read this book.
PLEASE LOOK AT THE ATTACHMENT. THANKS!

Target Market(s)

males, entrepreneurs, small business owners, salespeople, corporate executives

Industry/Entity Type

Business

Logo Text

VELVET ANVIL

Logo styles of interest
Emblem Logo
Abstract Logo
Font styles to use
Serif
Sans Serif

Colors
ec1f27
000000
959595
ffffff

Requirements
Must have
• It has to have a "hurricane" feel to it with hurricane colors.
Nice to have
• I open to your ideas
Should not have
• no other colors except red, black, gray, white.

```html
<!DOCTYPE html>
<html lang="en">
<head>
<meta charset="utf-8">
<title>Velvet Anvil – Book Cover</title>
<link rel="stylesheet" href="https://fonts.googleapis.com/css2?family=Bebas+Neue&family=Oswald:wght@300;600&family=Rubik+Dirt&display=swap">
<style>
  :root {
    --red: #e3070f;
    --ink: #111111;
    --storm-dark: #3a3a3a;
    --storm-mid: #6e6e6e;
    --storm-light: #d4d4d4;
    --paper: #ffffff;
    --backdrop: #ffffff;
  }
  html, body {
    margin: 0;
    padding: 0;
    width: 1200px;
    height: 1000px;
    overflow: hidden;
    background: var(--backdrop);
  }
  .canvas {
    position: relative;
    width: 1200px;
    height: 1000px;
  }
  .cover {
    position: absolute;
    left: 285px;
    top: 67px;
    width: 613px;
    height: 866px;
    background: var(--paper);
    overflow: hidden;
  }
  .storm-art {
    position: absolute;
    inset: 0;
    width: 613px;
    height: 866px;
  }
  .title-block {
    position: absolute;
    left: 48px;
    top: 478px;
  }
  .title {
    margin: 0;
    font-family: "Bebas Neue", "Oswald", sans-serif;
    font-weight: 400;
    font-size: 124px;
    line-height: 100px;
    color: var(--red);
    letter-spacing: 1px;
  }
  .title span { display: block; }
  .subtitle {
    margin: 20px 0 0;
    font-family: "Rubik Dirt", "Bebas Neue", sans-serif;
    font-size: 21px;
    line-height: 28px;
    color: var(--ink);
    letter-spacing: 0.3px;
  }
  .subtitle span { display: block; }
  .byline {
    margin: 22px 0 0;
    font-family: "Oswald", sans-serif;
    font-size: 27px;
    line-height: 30px;
    color: var(--ink);
    letter-spacing: 0.5px;
  }
  .byline .by { font-weight: 300; }
  .byline .author { font-weight: 600; }
</style>
</head>
<body>
<div class="canvas">
  <section class="cover">
    <svg class="storm-art" viewBox="0 0 613 866" role="img" aria-label="Abstract swirling storm of grey shards sweeping across the top and down the right side">
      <defs>
        <linearGradient id="stormFade" x1="0" y1="0" x2="0.35" y2="1">
          <stop offset="0" stop-color="var(--storm-dark)"/>
          <stop offset="0.45" stop-color="var(--storm-dark)"/>
          <stop offset="1" stop-color="var(--storm-mid)"/>
        </linearGradient>
        <linearGradient id="stormEdge" x1="0" y1="0" x2="1" y2="0.4">
          <stop offset="0" stop-color="var(--storm-light)" stop-opacity="0.9"/>
          <stop offset="1" stop-color="var(--storm-light)" stop-opacity="0"/>
        </linearGradient>
      </defs>
      <path fill="url(#stormEdge)" d="M0 225 C120 250 230 270 330 330 C420 395 470 520 470 866 L420 866 C420 560 360 420 250 340 C170 290 80 280 0 300 Z"/>
      <path fill="url(#stormFade)" d="M0 0 H613 V866 H500 C505 700 480 560 420 450 C360 345 260 290 140 272 C90 266 40 262 0 268 Z"/>
    </svg>
    <div class="title-block">
      <h1 class="title"><span>Velvet</span><span>Anvil</span></h1>
      <p class="subtitle"><span>HOW TO CLIMB PAST EVERY LIMIT</span><span>AT FULL THROTTLE</span></p>
      <p class="byline"><span class="by">BY</span> <span class="author">CAL DUNMORE</span></p>
    </div>
  </section>
</div>
</body>
</html>
```